Banner Designs for Drone Defense Ad Campaign

Corvane is a security consulting and services company that offers a service called SkyMindful. SkyMindful helps our customers identify security risks from drones and develops comprehensive protection programs. We are looking for a designer to create a banner ad in three sizes for our campaign.
Target Market(s)
Our campaign is geared to the sports and entertainment industry, specifically large event venues and their security operation.
Industry/Entity Type
Security
Font styles to use
Other font styles liked:
- Raleway
Requirements
Must have
- Banner Objective
The visual and textual content of the banner should prompt the viewer to quickly identify the service offered and the information that is available to download.
Banner Design
Logo: SkyMindful logo
Call to Action Button in Red: Get It Here (On Right or or Upper Right)
Title in Larger Font: Guide to UAS Risk Mitigation
Subtitle in smaller Font: 5 Steps to Develop Your Comprehensive UAS Defense Program
Background: Stadium with a drone flying in foreground
Font: Raleway
Banner Sizes
1 - 1200x670 pixels
2 - 1510x196 pixels
3 - 1200x628 pixels

```html
<!DOCTYPE html>
<html lang="en">
<head>
<meta charset="utf-8">
<title>SkyMindful – Guide to UAS Risk Mitigation</title>
<link href="https://fonts.googleapis.com/css2?family=Raleway:wght@500;700;800;900&display=swap" rel="stylesheet">
<style>
  :root {
    --page-grey: #979797;
    --title-blue: #63a6e6;
    --cta-red: #e0280f;
    --cta-red-dark: #b81808;
    --white: #ffffff;
    --night: #0f1a2a;
    --crowd: #3a1f24;
    --crowd-red: #5a2426;
    --pitch: #4f8a3c;
    --pitch-light: #6fa552;
  }
  * { box-sizing: border-box; margin: 0; padding: 0; }
  html, body { width: 1200px; height: 1200px; overflow: hidden; }
  body {
    background: var(--page-grey);
    font-family: "Raleway", sans-serif;
    position: relative;
  }
  .banner {
    position: absolute;
    left: 120px; top: 332px;
    width: 960px; height: 536px;
    overflow: hidden;
  }
  .stadium-photo {
    position: absolute; inset: 0;
    background:
      radial-gradient(ellipse 300px 120px at 410px 0, rgba(200,220,255,0.35), transparent 70%),
      linear-gradient(180deg, var(--night) 0%, #1d2436 22%, var(--crowd) 42%, var(--crowd-red) 62%, #3c4a3a 72%, var(--pitch) 80%, var(--pitch-light) 100%);
  }
  .brand {
    position: absolute;
    left: 90px; top: 62px;
    color: var(--white);
    text-align: right;
  }
  .brand-name {
    display: block;
    font-size: 32px; font-weight: 700;
    letter-spacing: -0.5px;
    line-height: 1;
  }
  .brand-parent {
    display: block;
    font-size: 17px; font-weight: 500;
    margin-top: 6px;
  }
  .cta {
    position: absolute;
    left: 636px; top: 52px;
    width: 286px; height: 53px;
    border-radius: 27px;
    background: linear-gradient(180deg, var(--cta-red) 0%, var(--cta-red-dark) 100%);
    color: var(--white);
    font-size: 30px; font-weight: 900;
    letter-spacing: 0.5px;
    display: flex; align-items: center; justify-content: center;
    text-decoration: none;
    box-shadow: 0 2px 4px rgba(0,0,0,0.35);
  }
  .title {
    position: absolute;
    left: 90px; top: 160px;
    color: var(--title-blue);
    font-size: 80px; font-weight: 900;
    line-height: 64px;
    letter-spacing: -3px;
    text-transform: uppercase;
  }
  .subtitle {
    position: absolute;
    left: 98px; top: 376px;
    color: var(--white);
    font-size: 30px; font-weight: 800;
    line-height: 36px;
    letter-spacing: -0.8px;
    text-transform: uppercase;
    text-shadow: 0 1px 3px rgba(0,0,0,0.5);
  }
</style>
</head>
<body>
  <section class="banner">
    <div class="stadium-photo" role="img" aria-label="Floodlit football stadium at night with a packed crowd and players on the pitch, a quadcopter drone with a camera flying in the foreground on the right"></div>

    <div class="brand">
      <span class="brand-name">SkyMindful</span>
      <span class="brand-parent">By Corvane</span>
    </div>

    <a class="cta" href="#">GET IT HERE</a>

    <h1 class="title">Guide to<br>UAS Risk<br>Mitigation</h1>

    <p class="subtitle">5 Steps to Develop Your<br>Comprehensive UAS<br>Defense Program</p>
  </section>
</body>
</html>
```